Need modern simple design for magazine ad, apartment and condo roofer.

I need a half page magazine ad for a local roofer to publish in an industry magazine. Apartment associations industry. All types of roofs. Shingle and Flat
Need the design to be creative and modern, clean and simple. I do not want a busy design. One that stands out and makes a point quickly.
Logo must be prominent.
DO NOT USE PHOTOS FROM MY WEBSITE PLEASE. Looking for something new.
I work on entire complexes not houses.

Need to make sure our phone number and email address are listed at the bottom. Here is my website www.vorbelan.com
Want to stay away from standard clip arts of tools, homes, apartment buildings.
Half Horizontal 7.25 x 4.75
Ads should be in PDF and JPG format.

Target Market(s)

Apartment or Condo owners looking for large scale roofing projects

Industry/Entity Type

Roofing

Requirements
Must have
• Prominent Logo
Simple Clean Design
Create graphics
Not Busy
Should not have
• Clip Art
No Photos from my website

```html
<!DOCTYPE html>
<html lang="en">
<head>
<meta charset="utf-8">
<title>Vorbelan Roofing – Half Page Ad</title>
<link href="https://fonts.googleapis.com/css2?family=Arimo:wght@700&family=Baloo+2:wght@700&display=swap" rel="stylesheet">
<style>
  :root{
    --stage:#f1f1f1;
    --paper:#ffffff;
    --frame-outer:#ececec;
    --frame-inner:#d9d9da;
    --brand-blue:#1f76c0;
    --brand-blue-soft:#6fa8d8;
    --brand-blue-pale:#c7dcee;
    --ink:#1a1a1a;
    --icon-grey:#8d8e92;
    --glow-violet:rgba(205,179,216,.7);
    --glow-grey:rgba(200,201,206,.45);
  }
  html,body{margin:0;padding:0;width:1200px;height:1200px;overflow:hidden;background:var(--stage);}
  .ad{
    position:absolute;left:64px;top:306px;width:1077px;height:590px;overflow:hidden;
    background:
      radial-gradient(ellipse 34% 42% at 33% 75%, var(--glow-violet), rgba(205,179,216,0) 72%),
      radial-gradient(ellipse 40% 35% at 52% 62%, var(--glow-grey), rgba(255,255,255,0) 75%),
      linear-gradient(180deg, #ffffff 0%, #f6f6f8 55%, #ffffff 100%);
  }
  .ad__frame-outer{position:absolute;left:28px;top:30px;width:1021px;height:531px;border:18px solid var(--frame-outer);box-sizing:border-box;}
  .ad__frame-inner{position:absolute;left:47px;top:46px;width:983px;height:493px;border:10px solid var(--frame-inner);box-sizing:border-box;}
  .ad__stripes{position:absolute;left:0;top:0;width:1077px;height:590px;}

  .brand{position:absolute;left:128px;top:139px;display:flex;align-items:center;gap:28px;}
  .brand__mark{width:92px;height:92px;background:var(--brand-blue);}
  .brand__name{font-family:"Arimo",Arial,sans-serif;font-weight:700;font-size:88px;line-height:1;color:var(--brand-blue);letter-spacing:-1px;white-space:nowrap;}

  .contact{font-family:"Baloo 2",sans-serif;font-weight:700;color:var(--ink);}
  .contact__row{position:absolute;left:358px;display:flex;align-items:center;gap:20px;}
  .contact__row--phone{top:350px;}
  .contact__row--email{top:408px;}
  .contact__row--address{top:465px;align-items:flex-start;}
  .contact__icon{width:38px;height:38px;flex:none;}
  .contact__text{font-size:32px;line-height:38px;white-space:nowrap;}
  .contact__text--address{font-size:25px;line-height:30px;}
</style>
</head>
<body>
<main class="ad">
  <div class="ad__frame-outer"></div>
  <div class="ad__frame-inner"></div>

  <svg class="ad__stripes" viewBox="0 0 1100 602" preserveAspectRatio="none" aria-hidden="true">
    <defs>
      <linearGradient id="fadeRight" x1="0" y1="0" x2="1" y2="1">
        <stop offset="0" stop-color="#ffffff" stop-opacity="0"/>
        <stop offset="1" stop-color="#1f76c0"/>
      </linearGradient>
      <linearGradient id="cornerBlue" x1="0" y1="1" x2="1" y2="0">
        <stop offset="0" stop-color="#ffffff" stop-opacity=".2"/>
        <stop offset=".6" stop-color="#2b80c6"/>
        <stop offset="1" stop-color="#1f76c0"/>
      </linearGradient>
    </defs>
    <g class="stripes-left">
      <polygon points="0,340 0,372 260,602 300,602" fill="#c7dcee" opacity=".7"/>
      <polygon points="56,364 258,543 215,543 56,404" fill="#1f76c0" opacity=".85"/>
      <polygon points="56,428 188,543 150,543 56,462" fill="#1f76c0" opacity=".75"/>
      <polygon points="56,492 114,543 84,543 56,518" fill="#1f76c0" opacity=".7"/>
      <polygon points="0,400 0,430 196,602 230,602" fill="#6fa8d8" opacity=".45"/>
      <polygon points="0,460 0,492 126,602 160,602" fill="#6fa8d8" opacity=".4"/>
      <polygon points="0,530 0,560 50,602 84,602" fill="#6fa8d8" opacity=".35"/>
    </g>
    <g class="stripes-right">
      <polygon points="810,322 850,322 1100,562 1100,602 1075,602" fill="url(#fadeRight)" opacity=".9"/>
      <polygon points="810,385 840,385 1060,602 1022,602" fill="url(#fadeRight)" opacity=".75"/>
      <polygon points="810,455 836,455 985,602 950,602" fill="url(#fadeRight)" opacity=".6"/>
      <polygon points="810,520 830,520 912,602 885,602" fill="url(#fadeRight)" opacity=".45"/>
      <polygon points="1100,417 1100,602 906,602" fill="url(#cornerBlue)"/>
    </g>
  </svg>

  <div class="brand">
    <div class="brand__mark"></div>
    <div class="brand__name">Vorbelan Roofing</div>
  </div>

  <div class="contact">
    <div class="contact__row contact__row--phone">
      <svg class="contact__icon" viewBox="0 0 40 40" aria-hidden="true">
        <circle cx="20" cy="20" r="19" fill="var(--icon-grey)"/>
        <rect x="13" y="9" width="12" height="21" rx="2" fill="none" stroke="#fff" stroke-width="1.8"/>
        <circle cx="19" cy="26" r="1.3" fill="#fff"/>
        <path d="M28 16a5 5 0 0 1 0 7M31 13a9 9 0 0 1 0 13" fill="none" stroke="#fff" stroke-width="1.4"/>
      </svg>
      <span class="contact__text">555.014.2290</span>
    </div>
    <div class="contact__row contact__row--email">
      <svg class="contact__icon" viewBox="0 0 40 40" aria-hidden="true">
        <circle cx="20" cy="20" r="19" fill="var(--icon-grey)"/>
        <rect x="10" y="15" width="20" height="14" fill="none" stroke="#fff" stroke-width="1.6"/>
        <path d="M10 15l10 8 10-8M10 29l7-6M30 29l-7-6" fill="none" stroke="#fff" stroke-width="1.6"/>
        <rect x="14" y="9" width="12" height="9" fill="var(--icon-grey)" stroke="#fff" stroke-width="1.4"/>
        <path d="M16 12h8M16 15h8" stroke="#fff" stroke-width="1.2"/>
      </svg>
      <span class="contact__text">info@vorbelan.com</span>
    </div>
    <div class="contact__row contact__row--address">
      <svg class="contact__icon" viewBox="0 0 40 40" aria-hidden="true">
        <circle cx="20" cy="20" r="19" fill="var(--icon-grey)"/>
        <path d="M20 29s-7-8-7-13a7 7 0 0 1 14 0c0 5-7 13-7 13z" fill="none" stroke="#fff" stroke-width="1.7"/>
        <circle cx="20" cy="16" r="2.5" fill="none" stroke="#fff" stroke-width="1.5"/>
        <path d="M13 32h14" stroke="#fff" stroke-width="1.5"/>
      </svg>
      <span class="contact__text contact__text--address">742 Meridian Avenue, Suite 210,<br>Harlow, TX 75510</span>
    </div>
  </div>
</main>
</body>
</html>
```